Redesign Login page

I want to redesign my login page to bring my 2 products closer together. I am only looking to redesign one login page, not 2.

For the logo, please make it solid and it can be black or white if helpful. I can also fine tune the logo if you get it close.

Coding

Coded - Design and coding required

Number of Pages Required

1 page

```html
<!DOCTYPE html>
<html lang="en">
<head>
<meta charset="utf-8">
<title>Login</title>
<link rel="stylesheet" href="https://fonts.googleapis.com/css2?family=Poppins:wght@400;500;600&display=swap">
<style>
:root{
  --bg:#f3f1ec;
  --ink:#1f1f1f;
  --muted:#3a3a3a;
  --brand:#4650e6;
  --link:#3b35c9;
  --brand-name:#9b2a1e;
  --field-border:#f1e4e2;
  --card-border:#ffffff;
  --blob-yellow:rgba(242,210,140,.95);
  --blob-red:rgba(236,150,140,.9);
  --blob-blue:rgba(160,205,240,.9);
}
*{box-sizing:border-box;margin:0;padding:0}
html,body{width:1200px;height:783px;overflow:hidden}
body{
  font-family:"Poppins",sans-serif;
  color:var(--ink);
  background:
    radial-gradient(ellipse 215px 280px at 335px 520px,var(--blob-yellow),rgba(242,210,140,0) 100%),
    radial-gradient(ellipse 225px 260px at 895px 315px,var(--blob-red),rgba(236,150,140,0) 100%),
    radial-gradient(ellipse 290px 160px at 745px 690px,var(--blob-blue),rgba(160,205,240,0) 100%),
    var(--bg);
  position:relative;
}
.brand{
  position:absolute;top:46px;left:0;width:100%;
  text-align:center;font-size:34px;font-weight:600;color:var(--brand-name);letter-spacing:-.5px
}
.login-card{
  position:absolute;left:362px;top:121px;width:476px;height:541px;
  border-radius:26px;border:1px solid var(--card-border);
  background:linear-gradient(160deg,rgba(255,255,255,.85),rgba(255,255,255,.55) 55%,rgba(240,246,255,.7));
  padding:0 42px;
}
.login-title{text-align:center;font-size:22.5px;font-weight:600;margin-top:42px;letter-spacing:-.2px;line-height:34px}
.field-label{display:block;font-size:12px;line-height:18px;margin-bottom:6px}
.field-user{margin-top:47px}
.field-pass{margin-top:25px}
.field-box{
  height:39px;border:1px solid var(--field-border);border-radius:5px;
  background:rgba(255,255,255,.55);
  display:flex;align-items:center;justify-content:space-between;padding:0 12px;
  font-size:12px;
}
.field-box .placeholder{color:var(--muted)}
.field-box .forgot{font-weight:500}
.options{display:flex;justify-content:space-between;align-items:center;margin-top:17px;font-size:12px}
.remember{display:flex;align-items:center;gap:7px;padding-left:3px}
.checkbox{width:14px;height:14px;border:1px solid #8a8a8a;border-radius:2px;background:#fff}
.enroll{color:var(--link)}
.login-btn{
  margin-top:51px;height:52px;border-radius:9px;background:var(--brand);
  color:#fff;font-size:15px;font-weight:500;display:flex;align-items:center;justify-content:center
}
.assist{text-align:center;font-size:13.3px;margin-top:56px}
.assist a{color:var(--link);font-weight:600;text-decoration:none}
</style>
</head>
<body>
<div class="brand">Korvane</div>
<main class="login-card">
  <h1 class="login-title">Login to your account</h1>
  <div class="field field-user">
    <span class="field-label">User ID</span>
    <div class="field-box"><span class="placeholder">Enter your ID</span><span class="forgot">Forgot ?</span></div>
  </div>
  <div class="field field-pass">
    <span class="field-label">Password</span>
    <div class="field-box"><span class="placeholder">Enter Password</span><span class="forgot">Forgot ?</span></div>
  </div>
  <div class="options">
    <label class="remember"><span class="checkbox"></span>Remember me</label>
    <span class="enroll">Enroll in online access</span>
  </div>
  <div class="login-btn">Login</div>
  <p class="assist">We’re Here to Assist You <a href="#">Get in Touch</a></p>
</main>
</body>
</html>
```